Boom Way Hoist Service Business Cards

I need a business card for "Boom Way Hoist and Haulage"

Boomway2023@hoistmail.net

Hoist Works LLC, Boom Way Hoist and Haulage LLC

555.014.7260 | www.BOOMWAYHOISTS.example

Riverbend County & Lakeshore County

(RB) 14820 Maple Lane Millbrook, RB 46000

(LS) 2450 Pell Street Harborview, LS 44300

Colors
0094D4
00A9DD
6FCCEA
C7EBF8
E9F6FB
59FF00
82FF00
B8FF75
E3FFCB
F4FFEA
EE7325
F08F49
F5BC92
FAE3D3
FDF4ED
EB3D1F
EC4F4E
F09395
F8D3D4
FCEDEE
E54698
E96AAD
F1A4CE
F9D9EA
FCEFF6
A7469A
B969AE
D3A5CF
EDDBEB
F8F0F9

```html
<!DOCTYPE html>
<html lang="en">
<head>
<meta charset="utf-8">
<title>Boom Way Hoist Service – Business Cards</title>
<link href="https://fonts.googleapis.com/css2?family=Archivo+Black&family=Questrial&display=swap" rel="stylesheet">
<style>
  :root {
    --page: #f2f2f2;
    --card: #000000;
    --ink: #ffffff;
    --accent: #3ab54a;
  }
  * { box-sizing: border-box; margin: 0; padding: 0; }
  html, body { width: 1060px; height: 1200px; overflow: hidden; background: var(--page); }
  .canvas { position: relative; width: 1060px; height: 1200px; }
  .card {
    position: absolute; left: 80px; width: 870px; height: 498px;
    background: var(--card); color: var(--ink); overflow: hidden;
  }
  .card--front { top: 82px; }
  .card--back { top: 618px; }

  .fleet-art {
    position: absolute; left: 0; top: 92px; width: 334px; height: 406px;
    background: linear-gradient(160deg, #2a2a2a 0%, #5a5a5a 40%, #c23a22 70%, #3ab54a 100%);
    opacity: .9;
  }

  .brand { position: absolute; display: flex; align-items: center; gap: 14px;
    font-family: "Archivo Black", sans-serif; color: var(--ink); text-transform: uppercase; }
  .brand__mark { flex: none; background: var(--accent); }
  .brand__name { line-height: 1.02; text-align: right; white-space: nowrap; }
  .card--front .brand { right: 140px; top: 28px; }
  .card--front .brand__mark { width: 22px; height: 22px; }
  .card--front .brand__name { font-size: 50px; }
  .card--back .brand { left: 200px; top: 124px; }
  .card--back .brand__mark { width: 36px; height: 36px; }
  .card--back .brand__name { font-size: 70px; }

  .details { position: absolute; right: 31px; font-family: "Questrial", sans-serif; text-align: right; }
  .details--company { top: 244px; font-size: 20px; }
  .contact { top: 286px; list-style: none; font-size: 21px; line-height: 31px; }
  .contact li { display: flex; justify-content: flex-end; align-items: center; gap: 10px; }
  .contact svg { width: 20px; height: 20px; fill: none; stroke: var(--accent); stroke-width: 2; }
  .address { top: 392px; font-size: 21px; line-height: 29px; }
</style>
</head>
<body>
<main class="canvas">
  <section class="card card--front">
    <div class="fleet-art" role="img" aria-label="Illustration of a red boom truck and a green mobile crane in front of a grey construction skyline"></div>
    <div class="brand">
      <span class="brand__mark"></span>
      <span class="brand__name">Boom Way<br>Hoist<br>Service</span>
    </div>
    <p class="details details--company">Hoist Works LLC, Boom Way Hoist and Haulage LLC</p>
    <ul class="details contact">
      <li>555.014.7260
        <svg viewBox="0 0 24 24"><path d="M5 3h4l2 5-2.5 1.5a11 11 0 0 0 6 6L16 13l5 2v4a2 2 0 0 1-2 2A16 16 0 0 1 3 5a2 2 0 0 1 2-2z"/></svg></li>
      <li>Boomway2023@hoistmail.net
        <svg viewBox="0 0 24 24"><rect x="3" y="6" width="18" height="12" fill="#3ab54a"/><path d="M3 6l9 7 9-7" stroke="#000"/></svg></li>
      <li>www.BOOMWAYHOISTS.example
        <svg viewBox="0 0 24 24"><circle cx="12" cy="12" r="9"/><path d="M3 12h18M12 3c3 3 3 15 0 18M12 3c-3 3-3 15 0 18"/></svg></li>
    </ul>
    <p class="details address">Riverbend County &amp; Lakeshore County<br>(RB) 14820 Maple Lane Millbrook, RB 46000<br>(LS) 2450 Pell Street Harborview, LS 44300</p>
  </section>

  <section class="card card--back">
    <div class="brand">
      <span class="brand__mark"></span>
      <span class="brand__name">Boom Way<br>Hoist<br>Service</span>
    </div>
  </section>
</main>
</body>
</html>
```